Artisan Food and Beverage company needs label for various product

We are an artisan food and beverage company with a range of different snacks, and beverages, such as chips, cold brew coffee and spreads. Because of this, we have different types of packaging - jars, pouches, bottles.
We are looking for a general label design for our different product ranges. We want to have a design that is adaptable to our different packaging containers but that will also distinguish each product from each other. Eg. Different colors for each product range
Our idea is to have the same general look for all but change the color of the border or sides(?) for each product range, We are thinking of something like this:
1. Border: different color per product range (see the collage pic and the screenshot taken from the Pixel Harbor website)
2. Product Category: Eg. Ice Cold Brew , Cheese Dips
- Same size font and type even if one is a pouch and 1 is a flask
3. Product Flavour: Eg. Mocha Latte, Cheddar and Garlic Dip
- Same size font and type even if different packaging (smaler size font
than the product category name
We have added sample pictures of a store label that fits different containers (collage pic) , as well as sample pics of our different packaging containers. We will also have jars for our spreads similar to the jar pic at the top of the collage.
If the design can be editable and the background color (or side color like the one we took a screenshot of here in the website of the crunchy sauce label - pardon that the drop down menu was taken), that is what we have in mind. We should also be able to edit the size so the best pf the whole label so maybe a rectangular label is best.
The "Chef Tobin's" is our official logo.
*Credits to the artist of the Pixel Harbor sample labels we took a screenshot of from the website.

```html
<!DOCTYPE html>
<html lang="en">
<head>
<meta charset="utf-8">
<title>Chef Tobin's Product Labels</title>
<link href="https://fonts.googleapis.com/css2?family=League+Spartan:wght@700&family=Open+Sans:wght@700&display=swap" rel="stylesheet">
<style>
  :root {
    --canvas: #ffffff;
    --cheese: #e6be22;
    --coffee: #6b4e39;
    --panel: #ffffff;
    --band: #463a2a;
    --ink: #000000;
    --brand: #d4853a;
    --flavour-cheese: #e6be22;
    --flavour-coffee: #e8903a;
  }
  html, body {
    margin: 0;
    padding: 0;
    width: 1200px;
    height: 632px;
    overflow: hidden;
    background: var(--canvas);
  }
  .sheet {
    position: relative;
    width: 1200px;
    height: 632px;
  }
  .label {
    position: absolute;
    top: 89px;
    width: 464px;
    height: 465px;
  }
  .label--cheese { left: 123px; }
  .label--coffee { left: 619px; }
  .label__pattern {
    position: absolute;
    inset: 0;
  }
  .label--cheese .label__pattern { background: var(--cheese); }
  .label--coffee .label__pattern { background: var(--coffee); }
  .label__panel {
    position: absolute;
    inset: 0;
    width: 464px;
    height: 465px;
  }
  .label__panel path { fill: var(--panel); }
  .brand {
    position: absolute;
    left: 0;
    width: 464px;
    top: 118px;
    text-align: center;
    font-family: "League Spartan", sans-serif;
    font-weight: 700;
    font-size: 24px;
    color: var(--brand);
    line-height: 1;
  }
  .category {
    position: absolute;
    left: 0;
    width: 464px;
    top: 220px;
    margin: 0;
    text-align: center;
    font-family: "League Spartan", sans-serif;
    font-weight: 700;
    font-size: 40px;
    color: var(--ink);
    line-height: 1;
  }
  .flavour {
    position: absolute;
    left: 101px;
    top: 283px;
    width: 263px;
    height: 56px;
    margin: 0;
    background: var(--band);
    display: flex;
    align-items: center;
    justify-content: center;
    font-family: "Open Sans", sans-serif;
    font-weight: 700;
    line-height: 1;
  }
  .label--cheese .flavour { color: var(--flavour-cheese); font-size: 21px; }
  .label--coffee .flavour { color: var(--flavour-coffee); font-size: 27px; }
</style>
</head>
<body>
<main class="sheet">
  <section class="label label--cheese">
    <div class="label__pattern" role="img" aria-label="Hand-drawn kitchen doodle pattern of peppers, cheese, herbs, cups and rolling pins in darker yellow"></div>
    <svg class="label__panel" viewBox="0 0 464 465" aria-hidden="true">
      <path d="M93,152 A23,23 0 0 1 116,129 H162 A73,73 0 1 1 304,129 H349 A23,23 0 0 1 372,152 V389 H93 Z"/>
    </svg>
    <div class="brand">Chef Tobin's</div>
    <h2 class="category">Cheese Dips</h2>
    <p class="flavour">Cheddar and Garlic Dip</p>
  </section>

  <section class="label label--coffee">
    <div class="label__pattern" role="img" aria-label="Hand-drawn kitchen doodle pattern of peppers, cheese, herbs, cups and rolling pins in light brown"></div>
    <svg class="label__panel" viewBox="0 0 464 465" aria-hidden="true">
      <path d="M93,152 A23,23 0 0 1 116,129 H162 A73,73 0 1 1 304,129 H349 A23,23 0 0 1 372,152 V389 H93 Z"/>
    </svg>
    <div class="brand">Chef Tobin's</div>
    <h2 class="category">Ice Cold Brew</h2>
    <p class="flavour">Mocha Latte</p>
  </section>
</main>
</body>
</html>
```